New Business Card Design Project VORASTI-Italy

we are VORASTI-Italy
our company in the market for 3 years we are luxury cosmetic company and its about time for a facelift :)
i will like to have elegant luxurious and unique business card
that will give the person that get it a unique, luxurious and elegant impression
I'm VERY OPEN FOR NEW IDEAS , even duo i add a few files of things that i see on line and i like them

i add my logo as well
my website is VORASTI.COM
(if you would like to see the main style that we have)

Target Market(s)

adult that have money :)

Industry/Entity Type

Business

Contact Information for Business Card

Name - Paul Vorasti
Position - CEO and CO Founder
address - 4817 E Larkdale
telephone - 555-384-1962
email - paul@vorasti.com
fax - 555-384-1962
website - VORASTI.COM

Colors
000000
959595
fbee3e
ffffff

Requirements
Must have
• big logo in GOLD color
• elegant look
• impressive
Nice to have
• not must but maybe classy pattern background
• not must but maybe emblem
• maybe clear plastic business card
Should not have
• colors
• images

```html
<!DOCTYPE html>
<html lang="en">
<head>
<meta charset="utf-8">
<title>VORASTI – Business Card</title>
<link href="https://fonts.googleapis.com/css2?family=Cinzel:wght@400;500&family=Josefin+Sans:wght@300;400&family=Roboto:wght@400&display=swap" rel="stylesheet">
<style>
  :root {
    --bg: #d9d9db;
    --card-light: #3b3b3c;
    --card-dark: #1d1d1e;
    --gold: #eeb04f;
    --ink: #2a2a2a;
  }
  * { margin: 0; padding: 0; box-sizing: border-box; }
  html, body { width: 1200px; height: 1200px; overflow: hidden; background: var(--bg); }
  .canvas { position: relative; width: 1200px; height: 1200px; }

  .card {
    position: absolute;
    left: 120px;
    width: 960px;
    height: 520px;
    background: radial-gradient(ellipse at 50% 45%, var(--card-light) 0%, var(--card-dark) 75%);
    color: var(--gold);
  }
  .card--front { top: 55px; }
  .card--back { top: 625px; }

  /* Front */
  .brand-front {
    position: absolute; left: 0; right: 0; top: 70px;
    display: flex; flex-direction: column; align-items: center;
  }
  .brand-ring {
    width: 170px; height: 170px; border-radius: 50%;
    border: 6px solid var(--gold);
  }
  .brand-name {
    margin-top: 40px;
    font-family: "Cinzel", serif; font-weight: 400;
    font-size: 104px; letter-spacing: 2px; line-height: 1;
    color: var(--gold);
  }
  .brand-rule { width: 560px; height: 4px; background: var(--gold); margin-top: 18px; }

  /* Back */
  .contact-side { position: absolute; left: 60px; top: 60px; width: 380px; }
  .holder-name {
    font-family: "Josefin Sans", sans-serif; font-weight: 400;
    font-variant: small-caps; font-size: 38px; letter-spacing: 1px;
    padding-left: 62px; line-height: 1;
  }
  .holder-rule { width: 300px; height: 2px; background: var(--gold); margin: 10px 0 6px 40px; }
  .holder-role {
    font-family: "Josefin Sans", sans-serif; font-weight: 300;
    font-variant: small-caps; font-size: 17px; letter-spacing: 1px;
    padding-left: 120px;
  }
  .contact-list { list-style: none; margin-top: 36px; }
  .contact-item {
    display: flex; align-items: center; gap: 14px;
    font-family: "Roboto", sans-serif; font-size: 22px;
    margin-bottom: 22px;
  }
  .contact-icon {
    width: 34px; height: 34px; border-radius: 6px;
    background: var(--gold); display: flex; align-items: center; justify-content: center;
    flex-shrink: 0;
  }
  .contact-icon svg { width: 22px; height: 22px; }
  .footer-rule { position: absolute; left: 130px; top: 440px; width: 290px; height: 2px; background: var(--gold); }
  .footer-flourish {
    position: absolute; left: 170px; top: 450px; width: 210px; height: 34px;
    background: linear-gradient(90deg, transparent, rgba(238,176,79,.45), transparent);
  }
  .divider { position: absolute; left: 470px; top: 50px; width: 3px; height: 420px; background: var(--gold); }
  .brand-back {
    position: absolute; left: 500px; right: 30px; top: 0; bottom: 0;
    display: flex; align-items: center; justify-content: center; gap: 24px;
  }
  .brand-back .brand-ring { width: 110px; height: 110px; border-width: 5px; }
  .brand-back .brand-name { margin: 0; font-size: 64px; }
</style>
</head>
<body>
<main class="canvas">
  <section class="card card--front">
    <div class="brand-front">
      <div class="brand-ring"></div>
      <div class="brand-name">VORASTI</div>
      <div class="brand-rule"></div>
    </div>
  </section>

  <section class="card card--back">
    <div class="contact-side">
      <div class="holder-name">Paul Vorasti</div>
      <div class="holder-rule"></div>
      <div class="holder-role">CEO and CO Founder</div>
      <ul class="contact-list">
        <li class="contact-item">
          <span class="contact-icon"><svg viewBox="0 0 24 24"><path d="M12 2a7 7 0 0 0-7 7c0 5 7 13 7 13s7-8 7-13a7 7 0 0 0-7-7zm0 9.5A2.5 2.5 0 1 1 12 6.5a2.5 2.5 0 0 1 0 5z" fill="var(--ink)"/></svg></span>
          4817 E Larkdale
        </li>
        <li class="contact-item">
          <span class="contact-icon"><svg viewBox="0 0 24 24"><path d="M6.6 10.8a15 15 0 0 0 6.6 6.6l2.2-2.2a1 1 0 0 1 1-.25 11 11 0 0 0 3.6.57 1 1 0 0 1 1 1V20a1 1 0 0 1-1 1A17 17 0 0 1 3 4a1 1 0 0 1 1-1h3.5a1 1 0 0 1 1 1c0 1.25.2 2.45.57 3.6a1 1 0 0 1-.25 1z" fill="var(--ink)"/></svg></span>
          555-384-1962
        </li>
        <li class="contact-item">
          <span class="contact-icon"><svg viewBox="0 0 24 24"><rect x="3" y="6" width="18" height="12" fill="none" stroke="var(--ink)" stroke-width="2"/><path d="M3 6l9 7 9-7" fill="none" stroke="var(--ink)" stroke-width="2"/></svg></span>
          paul@vorasti.com
        </li>
        <li class="contact-item">
          <span class="contact-icon"><svg viewBox="0 0 24 24"><rect x="7" y="3" width="10" height="5" fill="var(--ink)"/><rect x="3" y="9" width="18" height="8" rx="1" fill="var(--ink)"/><rect x="7" y="14" width="10" height="7" fill="var(--gold)" stroke="var(--ink)" stroke-width="2"/></svg></span>
          555-384-1962
        </li>
        <li class="contact-item">
          <span class="contact-icon"><svg viewBox="0 0 24 24"><circle cx="12" cy="12" r="9" fill="none" stroke="var(--ink)" stroke-width="2"/><ellipse cx="12" cy="12" rx="4" ry="9" fill="none" stroke="var(--ink)" stroke-width="1.6"/><path d="M3 12h18" stroke="var(--ink)" stroke-width="1.6"/></svg></span>
          vorasti.com
        </li>
      </ul>
    </div>
    <div class="footer-rule"></div>
    <div class="footer-flourish" role="img" aria-label="Decorative gold flourish ornament"></div>
    <div class="divider"></div>
    <div class="brand-back">
      <div class="brand-ring"></div>
      <div class="brand-name">VORASTI</div>
    </div>
  </section>
</main>
</body>
</html>
```